Accountancy firm needs clean and simple website and optional logo

We need a logo and basic wordpress website design for a Sydney based accountancy firm.
We need a clean and simple logo and website, based on the accounting/finance/tax industry. Simple, credible and official colors.
The logo is expected to be so simple that we have combined into the one job.
If you submit a logo design and we choose it along with someone else's website design you will be paid a bonus of $60. The website design will still win the competition as per normal.
Current website is old and terrible but gives you an idea of the sitemap (super simple) and what they do: www.helmwick.com.au
We want original different to normal template looking designs.
We like videos, and like http://www.marbeckers.com.au/
Feel free to go to reelmoss and use some videos from there.
We are based in Sydney Australia and in the field of taxation and accounting
We want a clean, formal, credible site, limited pages.
The project is guaranteed, so go for it.
Dorrit & Associates
1 page

```html
<!DOCTYPE html>
<html lang="en">
<head>
<meta charset="utf-8">
<title>Dorrit &amp; Associates – Tax Accountants</title>
<link rel="stylesheet" href="https://fonts.googleapis.com/css2?family=Raleway:wght@300;400;500;600;700&display=swap">
<style>
:root{
  --blue:#1289d6;
  --blue-deep:#0a56b8;
  --navy:#0b1f86;
  --ink:#111;
  --text:#333;
  --white:#fff;
  --paper:#f3f3f3;
  --rule:#cfcfcf;
}
*{box-sizing:border-box;margin:0;padding:0}
html,body{width:1200px;height:2299px;overflow:hidden}
body{position:relative;font-family:"Raleway",sans-serif;background:var(--white);color:var(--text)}
.abs{position:absolute}

.topbar{left:0;top:0;width:1200px;height:43px;background:var(--white)}
.topbar__phone{right:130px;top:7px;font-size:24px;color:var(--blue);font-weight:400}

.hero{left:0;top:43px;width:1200px;height:823px;overflow:hidden}
.hero__photo{position:absolute;inset:0;background:
  linear-gradient(180deg,rgba(0,0,0,.15) 0%,rgba(0,0,0,0) 30%,rgba(0,0,0,.25) 100%),
  linear-gradient(180deg,#8a8a3e 0%,#6f7a36 22%,#8c8a78 40%,#9e4a50 62%,#9b1e2c 78%,#7d1420 100%)}
.hero__rule{left:0;top:866px;width:1200px;height:8px;background:var(--rule)}
.brand{left:133px;top:64px;font-size:36px;font-weight:500;color:var(--white);line-height:1;letter-spacing:.5px}
.nav{top:97px;left:848px;display:flex;gap:36px}
.nav a{font-size:24px;color:var(--white);text-decoration:none;font-weight:400;padding-bottom:4px}
.nav a.is-active{border-bottom:3px solid var(--blue)}
.hero__title{left:127px;top:375px;font-size:48px;line-height:58px;font-weight:500;color:var(--white)}
.hero__cta{left:490px;top:628px;font-size:58px;font-weight:700;color:var(--white)}
.btn-call{left:490px;top:720px;width:499px;height:76px;background:linear-gradient(180deg,#1a9be6 0%,var(--blue-deep) 100%);color:var(--white);font-size:36px;font-weight:700;display:flex;align-items:center;justify-content:center}

.section-title{left:0;width:1200px;text-align:center;font-size:49px;font-weight:500;color:var(--ink);letter-spacing:.5px}
.service{width:360px}
.service__icon{display:block}
.service__label{font-size:37px;font-weight:300;color:#222;text-align:center}
.service-list{list-style:none}
.service-list li{position:absolute;font-size:16px;color:#333;white-space:nowrap;padding-left:33px;line-height:22px}
.tick{position:absolute;left:0;top:-2px}

.about{left:0;top:1395px;width:1200px;height:311px;background:var(--paper)}
.about__text{left:130px;top:1530px;width:940px;font-size:14.6px;line-height:24.5px;color:#333}

.client-photo{left:192px;top:1818px;width:132px;height:132px;border-radius:50%;background:radial-gradient(circle at 50% 45%,#d8a889 0%,#a76a4a 60%,#5e3a28 100%)}
.quote-mark{left:350px;top:1834px}
.quote-text{left:390px;top:1868px;width:600px;text-align:center;font-size:14px;line-height:18px;color:#222}
.dots{left:896px;top:1943px;display:flex;gap:11px}
.dots span{width:14px;height:14px;border-radius:50%;background:var(--blue)}
.dots span.is-current{background:#333}

.footer{left:0;top:2016px;width:1200px;height:283px;background:var(--navy);color:var(--white)}
.footer__head{font-size:14px;font-weight:500;color:var(--white)}
.footer__lines{font-size:11.5px;line-height:14.5px;color:var(--white)}
.social{display:flex;gap:24px}
.social span{width:32px;height:32px;border-radius:50%;border:2px solid var(--white)}
.copyright{left:133px;top:2240px;font-size:10px;color:var(--white)}
</style>
</head>
<body>

<header class="abs topbar">
  <div class="abs topbar__phone">Call us: 02 5550 1000</div>
</header>

<section class="abs hero">
  <div class="hero__photo" role="img" aria-label="Photograph of a smiling retired couple driving a red convertible, one waving a white hat, with green trees behind"></div>
</section>
<div class="abs hero__rule"></div>

<div class="abs brand">DORRIT &amp;<br>ASSOCIATES</div>
<nav class="abs nav">
  <a class="is-active" href="#">HOME</a>
  <a href="#">CONTACT</a>
</nav>
<h1 class="abs hero__title">Take The Worry Out of<br>Tax and Business</h1>
<div class="abs hero__cta">Let’s Get Started!</div>
<div class="abs btn-call">Call Now!</div>

<h2 class="abs section-title" style="top:910px">OUR SERVICES</h2>

<!-- Finance -->
<svg class="abs service__icon" style="left:228px;top:1025px" width="104" height="104" viewBox="0 0 104 104" aria-hidden="true">
  <g fill="#1289d6">
    <rect x="0" y="24" width="36" height="10" rx="3"/><rect x="0" y="37" width="36" height="10" rx="3"/>
    <rect x="0" y="50" width="36" height="10" rx="3"/><rect x="0" y="63" width="36" height="10" rx="3"/>
    <rect x="0" y="76" width="36" height="10" rx="3"/><rect x="0" y="89" width="36" height="10" rx="3"/>
    <rect x="62" y="0" width="40" height="10" rx="3"/><rect x="62" y="13" width="40" height="10" rx="3"/>
    <rect x="62" y="26" width="40" height="10" rx="3"/><rect x="62" y="39" width="40" height="10" rx="3"/>
    <rect x="62" y="52" width="40" height="10" rx="3"/><rect x="62" y="65" width="40" height="10" rx="3"/>
    <rect x="62" y="78" width="40" height="10" rx="3"/>
    <circle cx="52" cy="54" r="34"/>
  </g>
  <circle cx="52" cy="54" r="24" fill="#fff"/>
  <circle cx="52" cy="54" r="19" fill="#1289d6"/>
  <text x="52" y="66" text-anchor="middle" font-family="Raleway,sans-serif" font-weight="700" font-size="32" fill="#fff">$</text>
</svg>
<div class="abs service__label" style="left:101px;top:1127px;width:360px">Finance</div>

<!-- Filing -->
<svg class="abs service__icon" style="left:557px;top:1025px" width="84" height="102" viewBox="0 0 84 102" aria-hidden="true">
  <g fill="#fff" stroke="#1289d6" stroke-width="5">
    <rect x="28" y="4" width="50" height="70"/>
    <rect x="16" y="14" width="50" height="72"/>
    <rect x="4" y="24" width="52" height="74"/>
  </g>
  <g stroke="#1289d6" stroke-width="4">
    <line x1="14" y1="42" x2="46" y2="42"/><line x1="14" y1="52" x2="46" y2="52"/>
    <line x1="14" y1="62" x2="46" y2="62"/><line x1="14" y1="72" x2="46" y2="72"/>
    <line x1="14" y1="82" x2="46" y2="82"/>
  </g>
</svg>
<div class="abs service__label" style="left:418px;top:1127px;width:360px">Filing</div>

<!-- Services -->
<svg class="abs service__icon" style="left:860px;top:1020px" width="104" height="104" viewBox="0 0 104 104" aria-hidden="true">
  <circle cx="36" cy="36" r="26" fill="none" stroke="#1289d6" stroke-width="12" stroke-dasharray="9 6.3"/>
  <circle cx="36" cy="36" r="22" fill="#1289d6"/>
  <circle cx="36" cy="36" r="9" fill="#fff"/>
  <circle cx="76" cy="74" r="20" fill="none" stroke="#1289d6" stroke-width="10" stroke-dasharray="7 5.6"/>
  <circle cx="76" cy="74" r="17" fill="#1289d6"/>
  <circle cx="76" cy="74" r="7" fill="#fff"/>
</svg>
<div class="abs service__label" style="left:742px;top:1127px;width:360px">Services</div>

<svg width="0" height="0" style="position:absolute">
  <defs>
    <symbol id="tick" viewBox="0 0 26 24"><path d="M1 13 L6 9 L10 15 L22 1 L26 4 L10 23 Z" fill="#1289d6"/></symbol>
  </defs>
</svg>

<ul class="service-list">
  <li style="left:133px;top:1194px"><svg class="tick" width="26" height="24"><use href="#tick"/></svg>Tax Planning &amp; Returns</li>
  <li style="left:133px;top:1224px"><svg class="tick" width="26" height="24"><use href="#tick"/></svg>Residential Loans &amp; Financing</li>
  <li style="left:133px;top:1254px"><svg class="tick" width="26" height="24"><use href="#tick"/></svg>Superannuation Self-managed Funds</li>
  <li style="left:133px;top:1284px"><svg class="tick" width="26" height="24"><use href="#tick"/></svg>Estate Planning Together &amp; Succession</li>
  <li style="left:133px;top:1314px"><svg class="tick" width="26" height="24"><use href="#tick"/></svg>Financial &amp; Retirement Planning</li>

  <li style="left:449px;top:1194px"><svg class="tick" width="26" height="24"><use href="#tick"/></svg>GST Preparation &amp; Lodgement</li>
  <li style="left:449px;top:1224px"><svg class="tick" width="26" height="24"><use href="#tick"/></svg>Non-resident companies &amp; Trusts</li>
  <li style="left:449px;top:1254px"><svg class="tick" width="26" height="24"><use href="#tick"/></svg>Business Setup</li>
  <li style="left:449px;top:1284px"><svg class="tick" width="26" height="24"><use href="#tick"/></svg>Accounting System Establishment</li>
  <li style="left:449px;top:1314px"><svg class="tick" width="26" height="24"><use href="#tick"/></svg>Bookkeeping and Administration</li>

  <li style="left:771px;top:1194px"><svg class="tick" width="26" height="24"><use href="#tick"/></svg>Litigation Assistance</li>
  <li style="left:771px;top:1224px"><svg class="tick" width="26" height="24"><use href="#tick"/></svg>Business Advisory Services</li>
  <li style="left:771px;top:1254px"><svg class="tick" width="26" height="24"><use href="#tick"/></svg>Asset Protection Services</li>
  <li style="left:771px;top:1284px"><svg class="tick" width="26" height="24"><use href="#tick"/></svg>Business Recovery Services</li>
  <li style="left:771px;top:1314px"><svg class="tick" width="26" height="24"><use href="#tick"/></svg>Specialised Investment Administration</li>
</ul>

<section class="abs about"></section>
<h2 class="abs section-title" style="top:1430px">ABOUT US</h2>
<p class="abs about__text">Lorem ipsum dolor sit amet, consectetur adipiscing elit. Maecenas id nunc quis dui mattis tincidunt.. Aenean ex urna, accumsan ut urna id, facilisis lacinia eros. Duis fermentum, justo nec pulvinar dictum, massa libero faucibus elit, at dignissim ligula velit non neque. Pellentesque cursus aliquam sapien vel vehicula. Praesent a quam justo. Phasellus pellentesque nulla eu augue malesuada bibendum Cras at lectus elementum, fermentum arcu sed, ultrices neque.Etiam justo leo, interdum sit amet lorem nec,condimentum tincidunt mauris.Proin urna sem, vehicula vel finibus nec, ultricies quis erat. Fusce consectetur metus sed nisi ullamcorper elementum.</p>

<h2 class="abs section-title" style="top:1742px">WHAT OUR CLIENTS SAY</h2>
<div class="abs client-photo" role="img" aria-label="Round portrait photo of a smiling client with glasses"></div>
<svg class="abs quote-mark" width="46" height="34" viewBox="0 0 46 34" aria-hidden="true">
  <path d="M2 32 C2 16 8 6 20 2 L21 7 C13 10 11 15 11 18 L19 18 L19 32 Z M25 32 C25 16 31 6 43 2 L44 7 C36 10 34 15 34 18 L42 18 L42 32 Z" fill="#1289d6"/>
</svg>
<p class="abs quote-text">Curabitur odio quam, volutpat eget purus vel, gravida facilisis orc Aliquam posuere tincidunt mauris, quis suscipit ipsum sagittis in.i</p>
<div class="abs dots"><span></span><span class="is-current"></span><span></span><span></span></div>

<footer class="abs footer"></footer>
<div class="abs footer__head" style="left:329px;top:2050px">LOCATION</div>
<div class="abs footer__lines" style="left:332px;top:2075px">Dorrit &amp; Associates<br>ABN 00 000 000 000<br>Suite 12, 40 Harbour Lane<br>Fernvale, NSW 2099<br><br>Phone: +61 (2) 5550 1000<br>Fax: +61 (2) 5550 9999</div>
<div class="abs footer__head" style="left:567px;top:2053px">LINKS</div>
<div class="abs footer__lines" style="left:570px;top:2077px">Home<br>Contact<br>Privacy<br>Disclaimer</div>
<div class="abs footer__head" style="left:731px;top:2053px">LET’S CONNECT</div>
<div class="abs social" style="left:726px;top:2086px"><span></span><span></span><span></span></div>
<div class="abs copyright">Copyright 2015 - Dorrit &amp; Associates</div>

</body>
</html>
```